Holvery Real Estate Management Consulting

To design a high end company profile that inspires confidence in high net worth individuals and similar clients. The profile to include real estate images, preferably real images. The firm is a Zambian firm and has its target to be comparable to Tesk & Company, Parlowe & Company, Wilder Osten, Lun dorv pelsin wilder osten, TLAV Real estate company as such.

Target Market(s)

Real estate clients such as high net worth individuals, private and public companies, government and international agencies, banks and insurance companies, trusts and pension funds and individual investors. the sub target market group being developers, planners, financiers, market analysts, designers, economists, engineers, architects, construction managers, quantity surveyors and public officials and others

Colors

Designer to choose colors to be used in the design.

Requirements
Must have
• Company logo

```html
<!DOCTYPE html>
<html lang="en">
<head>
<meta charset="utf-8">
<title>Holvery Real Estate – Company Profile</title>
<link href="https://fonts.googleapis.com/css2?family=Roboto+Condensed:wght@400;700&family=Open+Sans:wght@400;600;700&display=swap" rel="stylesheet">
<style>
:root{
  --stage:#e3e3e3;
  --label:#4a4a4a;
  --brand:#3a4fa6;
  --brand-deep:#243a8f;
  --brand-light:#5a72c8;
  --ink:#3a3a3a;
  --muted:#6b6b6b;
  --panel-grey:#707070;
  --table-head:#c8c8c8;
  --table-row:#ececec;
  --white:#ffffff;
}
*{box-sizing:border-box;margin:0;padding:0}
html,body{width:1120px;height:1200px;overflow:hidden;background:var(--stage)}
body{position:relative;font-family:"Open Sans",sans-serif;color:var(--ink)}
.spread-label{position:absolute;width:344px;text-align:center;font-family:"Roboto Condensed",sans-serif;font-weight:700;font-size:37px;color:var(--label)}
.page{position:absolute;width:344px;height:444px;overflow:hidden;background:var(--white)}
.photo{position:absolute}
.abs{position:absolute}
.wordmark{font-family:"Roboto Condensed",sans-serif;font-weight:400;color:var(--white);letter-spacing:1px;line-height:1}
.tiny{font-size:4.2px;line-height:1.3;text-align:justify}
/* front */
.cover-photo{inset:0;background:linear-gradient(180deg,#4f7ed0 0%,#8aa7d8 30%,#6a6a78 55%,#3e4e3a 80%,#2b3b26 100%)}
.cover-title{right:12px;top:62px;text-align:right;font-family:"Roboto Condensed",sans-serif;color:var(--white);font-size:17px;line-height:1.05}
.cover-tagline{left:20px;top:400px;font-family:"Roboto Condensed",sans-serif;color:var(--white);font-size:21px}
/* back */
.back-page{background:var(--brand)}
.back-contact{left:0;right:0;top:385px;text-align:center;color:#dfe5ff;font-size:4.4px;line-height:1.35}
/* inner pages */
.tag-box{background:rgba(58,79,166,.88);color:var(--white);font-family:"Roboto Condensed",sans-serif;font-size:16px;padding:4px 0;letter-spacing:.5px}
.band{left:0;width:344px;background:var(--brand);color:var(--white)}
.section-head{font-family:"Roboto Condensed",sans-serif;font-weight:700;font-size:6.5px;display:flex;align-items:center;gap:5px}
.section-head::after{content:"";flex:0 0 70px;height:.6px;background:currentColor}
.services-table{left:17px;width:310px;border-collapse:collapse;font-size:4.2px;color:var(--muted)}
.services-table th{background:var(--table-head);font-family:"Roboto Condensed",sans-serif;font-weight:700;font-size:6.5px;color:var(--ink);padding:4px 6px;text-align:left}
.services-table th+th{text-align:center}
.services-table td{background:var(--table-row);padding:5px 6px;border-top:2px solid var(--white);vertical-align:middle;line-height:1.3}
.services-table td:first-child{width:68px;border-right:1px solid var(--white)}
.solutions{left:17px;width:310px;top:380px;height:64px;background:var(--panel-grey);color:#eee;padding:4px 8px}
.solutions h3{font-family:"Roboto Condensed",sans-serif;font-weight:400;font-size:7.5px;color:var(--white);display:flex;align-items:center;gap:4px;margin-bottom:2px}
.solutions h3::after{content:"";width:90px;height:.6px;background:#ddd}
.blue-head{font-family:"Roboto Condensed",sans-serif;font-weight:700;color:var(--brand);display:flex;align-items:center;gap:4px}
.blue-head.rule::after{content:"";flex:0 0 60px;height:.6px;background:var(--brand)}
.bullets{list-style:none;font-size:4.2px;line-height:1.4;color:var(--ink)}
.bullets li::before{content:"\2022 ";color:var(--brand)}
</style>
</head>
<body>

<div class="spread-label" style="left:158px;top:54px">Front</div>
<div class="spread-label" style="left:667px;top:54px">Back</div>
<div class="spread-label" style="left:158px;top:618px">Page 1</div>
<div class="spread-label" style="left:667px;top:618px">Page 2</div>

<!-- Front cover -->
<section class="page front-cover" style="left:158px;top:112px">
  <div class="photo cover-photo" role="img" aria-label="Photograph of high-rise residential towers above landscaped gardens under a blue sky"></div>
  <svg class="abs" width="344" height="444" viewBox="0 0 344 444" style="left:0;top:0">
    <polygon points="0,0 280,0 0,210" fill="#2a44a8" opacity=".55"/>
    <polygon points="180,0 344,0 344,110" fill="#2a44a8" opacity=".5"/>
    <polygon points="0,444 0,330 120,444" fill="#2a44a8" opacity=".35"/>
  </svg>
  <div class="abs wordmark" style="left:22px;top:62px;font-size:24px">Holvery</div>
  <div class="abs cover-title">HOLVERY REAL ESTATE<br>Management Consulting</div>
  <div class="abs cover-tagline">Accelerate Success....</div>
</section>

<!-- Back cover -->
<section class="page back-page" style="left:667px;top:112px">
  <svg class="abs" width="344" height="444" viewBox="0 0 344 444" style="left:0;top:0">
    <polygon points="0,0 170,0 344,200 344,444 0,444" fill="#2f46a0"/>
    <polygon points="200,0 344,0 344,330" fill="#4a64c0" opacity=".7"/>
    <polygon points="0,240 0,444 180,444" fill="#3550b0" opacity=".6"/>
  </svg>
  <div class="abs wordmark" style="left:0;right:0;top:342px;text-align:center;font-size:24px">Holvery</div>
  <div class="abs back-contact">
    Messrs. Holvery | Management Consulting<br>
    Unit 4 of Plot No. 2210<br>
    Meridian Road<br>
    Kafue, Lusaka<br><br>
    Mobile: +260 955 000 147 / 0955000148<br>
    E-mail: info@holveryconsulting.example
  </div>
</section>

<!-- Page 1 -->
<section class="page page-one" style="left:158px;top:676px">
  <div class="photo" style="left:0;top:0;width:344px;height:227px;background:linear-gradient(180deg,#f2f0ec 0%,#e2ddd6 55%,#b89a78 100%)" role="img" aria-label="Photograph of a family being welcomed into a bright home by an agent"></div>
  <svg class="abs" width="44" height="40" style="left:0;top:0"><polygon points="0,0 44,0 0,40" fill="var(--brand)"/></svg>
  <div class="abs tag-box" style="left:212px;top:151px;width:132px;text-align:center">INSPIRE VALUE</div>
  <div class="abs band" style="top:227px;height:52px;padding:6px 17px">
    <div class="section-head">WHO WE ARE</div>
    <p class="tiny" style="margin-top:4px;color:#e6e9f7">Holvery | Management Consulting is one of Zambia's leading professional real estate services firms with an outstanding reputation and has its cornerstone the excellence of its people. Since its inception, the business has continued successfully with a national client base, a number of which have retained our services.</p>
  </div>
  <table class="abs services-table" style="top:289px">
    <tr><th>Core Services</th><th>Scope</th></tr>
    <tr><td>Consulting</td><td>Advisory Services, Acquisition, Leasing &amp; Disposal Advice, Business Plans, Feasibility studies, Highest and Best Use Studies, Market research/analysis, Planning and development, Property Condition Assessments</td></tr>
    <tr><td>Valuations</td><td>Agriculture Valuations, Asset Valuations, Commercial Valuations, Leisure/Hotels/Lodges, Industrial Valuations, Special purpose Valuations, Mines Valuations, Residential Valuations, Plant, Machinery &amp; Equipment</td></tr>
    <tr><td>Firm's Reference</td><td>Surveyors Registration Council P.O Box 40118 Lusaka</td></tr>
  </table>
  <div class="abs solutions">
    <h3>&ldquo;Our Solutions</h3>
    <p class="tiny">As a preferred property firm we continually monitor property value levels and will provide you with an update on market rents, trends and the position of your property in the marketplace. We continue to roll out our real estate services for you so clients benefit from our experience and database. Our system allows you to save on research costs and time while all due diligence is done in identifying the interests, benefits and rights being researched. We assure our clients that our work is independent, objective and compliant with nationally recognized Laws of the Republic of Zambia.</p>
  </div>
</section>

<!-- Page 2 -->
<section class="page page-two" style="left:667px;top:676px">
  <div class="photo" style="left:0;top:0;width:201px;height:209px;background:linear-gradient(160deg,#e8e6e0 0%,#c9bfb2 50%,#6f7fa0 100%)" role="img" aria-label="Photograph of a couple reviewing documents with a consultant"></div>
  <div class="photo" style="left:205px;top:0;width:133px;height:98px;background:linear-gradient(180deg,#f4f4f4 0%,#d9cfc6 60%,#b8a89a 100%)" role="img" aria-label="Photograph of a hand holding a small model house and keys"></div>
  <svg class="abs" width="44" height="40" style="left:0;top:0"><polygon points="0,0 44,0 0,40" fill="var(--brand)"/></svg>
  <div class="abs tag-box" style="left:0;top:151px;width:126px;text-align:center">SMART MOVE</div>

  <div class="abs" style="left:206px;top:107px;width:130px">
    <div class="blue-head" style="font-size:7px;font-weight:400">Property Consultancy</div>
    <p class="tiny" style="margin-top:4px">As the property market has matured, we have provided consultancy advice to clients in the areas of relocation, market overview, research, planning and development, and property investment.</p>
    <div class="blue-head" style="font-size:7px;margin-top:4px;font-weight:400">Our consultancy services include</div>
    <ul class="bullets" style="margin-top:3px">
      <li>Acquisition, Leasing and Disposal advice</li>
      <li>Facilities Management advisory</li>
      <li>Highest and Best Use Studies</li>
      <li>Landlord and Tenant representation</li>
      <li>Market research/analysis</li>
      <li>Planning and development</li>
      <li>Property management advisory</li>
    </ul>
  </div>

  <div class="abs" style="left:11px;top:220px;width:322px">
    <div class="blue-head rule" style="font-size:6.5px">SERVICES AND BUSINESS LINES</div>
    <p class="tiny" style="margin-top:3px">Holvery Mgt Consulting serves our clients through four main business lines with services for all property types and asset classes.</p>
    <div class="blue-head rule" style="font-size:7.5px;font-weight:400;margin-top:4px">Advisory Services</div>
    <p class="tiny" style="margin-top:4px">Our advisory services help communities find strategic practical solutions for the most challenging issues facing today's urban, suburban and rural areas. We provide expert, independent, timely, candid, and biased-free input from national real estate, land use, design and planning experts. We help communities gain fresh insight and come to innovative solutions for complex land use and real estate development challenges. Our work aims to work with local governments, private developers, community development corporations and many other organizations to address the most challenging real estate and land use issues facing the communities today. Holvery Mgt consulting works with industry leaders including developers, planners, financiers, market analysts, designers, economists, engineers, architects, construction managers, quantity surveyors and public officials to provide practical and objective advice that is not available from any other source.</p>
    <div class="blue-head rule" style="font-size:7.5px;font-weight:400;margin-top:8px">Urban Planning and Development</div>
    <p class="tiny" style="margin-top:4px">Urban planning and development involves the design and organization of urban space and activities. We undertake due diligence and feasibility studies for landowners, developers and investors as regards the processes and considerations involved in development. We also undertake market analysis and demand forecasting; development feasibility and risk assessment; and make recommendations on how to implement an effective development project, including marketing and attracting potential development partners.</p>
  </div>

  <div class="abs" style="left:14px;top:357px;width:172px">
    <div class="blue-head rule" style="font-size:7.5px;font-weight:400">Valuation Services</div>
    <p class="tiny" style="margin-top:3px">Holvery Mgt provides comprehensive valuation, advisory and consulting services for real estate owners, investors and lenders, combining our specialized expertise and premier technologies to deliver industry-leading valuation reports and analysis. We focus on the valuation of various land and building assets, including agricultural, commercial, industrial, residential, retail, development sites and specialized properties. We act for private and public companies, government and international agencies, banks and insurance companies, trusts and pension funds and individual investors.</p>
  </div>

  <div class="abs" style="left:195px;top:357px;width:145px">
    <div class="blue-head" style="font-size:7.5px;font-weight:400">Uses of Valuation Services:</div>
    <div style="display:flex;gap:8px;margin-top:3px">
      <ul class="bullets">
        <li>Auction reserves valuations</li>
        <li>Collateral Valuations</li>
        <li>Financial Reporting</li>
        <li>Insurance Valuations</li>
      </ul>
      <ul class="bullets">
        <li>Legal/ Judgment purposes</li>
        <li>Property Transfer Tax</li>
        <li>Purchase and/or Sale among others</li>
        <li>Rental Valuations</li>
      </ul>
    </div>
  </div>

  <div class="abs" style="left:190px;top:417px;width:154px;height:27px;background:var(--brand)"></div>
</section>

</body>
</html>
```